Coupons App Design Project

We have a simple coupons app with few screens and actions:
1. Very simple login screen (with trellipo and vandro+)
2. Very simple business search page
3. Very simple business search results(each result contains logo icon, business name and delete icon)
4. business list (every row contains logo icon, business name and delete icon)
5. coupons list (each item contains image, title, subtitle, description, expiration time, status graphics (valid, expired, redeemed), delete icon
6. coupon view (image, title, subtitle, description, barcode etc.)
7. custom confirmation dialog(title, buttons, background, text)
8. "scan to subscribe" page (merchant name, merchant number, background image, text, barcode to scan etc.)
9. simple menu
10. splash screen

all graphics should be vector graphics so we can use it to different resolutions including for printing
Updates

Hi all, We've increased the project's budget by 25%. Thanks

Hi all,

We've decided to change the project from refundable to committed payment.
FYI

Hi All,

Thank you for your time and efforts, we really appreciate it.However we've eliminated most of the offered designs we've received becausethey didn't fit our desired look and feel.

Please download our look and feel file from our uploaded files -we've put there some examples of other apps that we like.

Thanks

Target Market(s)

shoppers all over the world

Industry/Entity Type

Business

Requirements
Must have
• Please take a look at the attached file "look & feel.jpg" for some nice screen shots taken from apps that we like

http://www.plinkforgeo.com/file.aspx?fileLocation=storage_url/brief_uploads/166833_09lookandfeel_brief010902.jpg
Should not have
• *****************************************************************************************
The attached files are only for demonstration purpose and needs descriptions so please don't send us design based on these screenshots.
*****************************************************************************************

```html
<!DOCTYPE html>
<html lang="en">
<head>
<meta charset="utf-8">
<title>Coupons App – Business Search Screens</title>
<link rel="stylesheet" href="https://fonts.googleapis.com/css2?family=Quicksand:wght@400;500&display=swap">
<style>
  :root {
    --stage-bg: #231f20;
    --brand-green: #a7d369;
    --screen-white: #ffffff;
    --screen-fade: #f4f4f4;
    --text-strong: #222222;
    --text-mid: #777777;
    --text-soft: #8a8a8a;
    --text-faint: #c9c9c9;
    --rule: #e2e2e2;
    --field-border: #a9a9a9;
    --icon-faint: #d6d6d6;
    --footer-grey: #959595;
    --thumb-blue: #7ccbee;
    --thumb-violet: #b9b4f0;
    --thumb-grey: #989898;
    --thumb-peach: #f2c4b7;
  }
  * { box-sizing: border-box; margin: 0; padding: 0; }
  html, body {
    width: 1200px; height: 691px; overflow: hidden;
    background: var(--stage-bg);
    font-family: "Quicksand", sans-serif;
  }
  .stage {
    position: relative; width: 1184px; height: 682px;
    transform: scale(1.0135); transform-origin: 0 0;
  }
  .screen {
    position: absolute; width: 374px; height: 567px; overflow: hidden;
    background: linear-gradient(to bottom, var(--screen-white) 0%, var(--screen-white) 60%, var(--screen-fade) 100%);
  }
  .screen--empty { left: 4px; top: 11px; }
  .screen--results { left: 403px; top: 9px; }
  .screen--swiped { left: 806px; top: 10px; }

  .app-bar {
    position: absolute; left: 0; top: 0; width: 100%; height: 62px;
    background: var(--brand-green);
  }
  .app-bar__title {
    position: absolute; left: 0; right: 0; top: 15px; text-align: center;
    color: #fff; font-size: 25px; font-weight: 400;
  }
  .app-bar__back { position: absolute; left: 11px; top: 11px; }
  .app-bar__settings { position: absolute; right: 9px; top: 11px; }

  .session-note {
    position: absolute; left: 0; right: 0; top: 68px; text-align: center;
    font-size: 13px; color: var(--text-mid);
  }
  .session-rule {
    position: absolute; left: 14px; width: 346px; top: 91px; height: 2px; background: var(--rule);
  }
  .page-title {
    position: absolute; left: 0; right: 0; top: 116px; text-align: center;
    font-size: 27px; color: var(--text-mid); font-weight: 400;
  }
  .search-field {
    position: absolute; left: 40px; top: 165px; width: 317px; height: 35px;
    border: 3px solid var(--field-border); background: #fff;
  }
  .search-field__text {
    position: absolute; left: 11px; top: 5px; font-size: 14px; color: var(--text-mid);
  }
  .search-field__icon { position: absolute; right: 8px; top: 4px; }

  .hint {
    position: absolute; left: 60px; right: 60px; top: 226px; text-align: center;
    font-size: 13px; line-height: 18px; color: var(--text-mid);
  }
  .empty-row {
    position: absolute; left: 20px; width: 336px; top: 360px; height: 66px;
    border-top: 3px solid var(--rule); border-bottom: 3px solid var(--rule);
  }
  .empty-row__mark {
    position: absolute; left: 1px; top: 5px; width: 20px; height: 53px; background: var(--thumb-blue);
  }
  .empty-row__title { position: absolute; left: 67px; top: 15px; font-size: 18px; color: var(--text-strong); }
  .empty-row__note { position: absolute; left: 67px; top: 37px; font-size: 10px; color: var(--text-soft); }

  .results-summary { position: absolute; left: 29px; top: 224px; font-size: 14px; line-height: 15px; }
  .results-summary__count { color: var(--text-mid); }
  .results-summary__tip { color: var(--text-faint); }

  .result-list {
    position: absolute; left: 14px; width: 336px; top: 266px; list-style: none;
    border-top: 3px solid var(--rule);
  }
  .result {
    position: relative; height: 65px; border-bottom: 3px solid var(--rule);
  }
  .result__logo {
    position: absolute; left: 1px; top: 4px; width: 57px; height: 53px;
  }
  .result__name { position: absolute; left: 68px; top: 14px; font-size: 16px; color: var(--text-strong); }
  .result__meta { position: absolute; left: 68px; top: 35px; font-size: 9px; color: var(--text-soft); }
  .result--swiped .result__logo { left: 124px; }
  .result--swiped .result__name,
  .result--swiped .result__meta { left: 190px; }
  .result__actions {
    position: absolute; left: 0; top: 0; width: 118px; height: 62px;
    border-right: 3px solid var(--rule);
  }
  .action-button {
    position: absolute; top: 11px; width: 41px; height: 41px;
    border: 2px solid var(--icon-faint); background: #fff;
    display: flex; align-items: center; justify-content: center;
  }
  .action-button--edit { left: 6px; }
  .action-button--delete { left: 57px; }

  .logo-blue { background: var(--thumb-blue); }
  .logo-violet { background: var(--thumb-violet); }
  .logo-grey { background: var(--thumb-grey); }
  .logo-peach { background: var(--thumb-peach); }

  .show-all {
    position: absolute; left: 0; bottom: 0; width: 100%; height: 25px;
    background: var(--footer-grey); color: #fff; font-size: 17px;
    display: flex; align-items: center; justify-content: center; gap: 14px;
  }
</style>
</head>
<body>
<main class="stage">

  <!-- Screen: empty search -->
  <section class="screen screen--empty">
    <header class="app-bar">
      <svg class="app-bar__back" width="40" height="40" viewBox="0 0 40 40"><circle cx="20" cy="20" r="17.5" fill="none" stroke="#fff" stroke-width="3"/><path d="M11 20h18M18 12l-8 8 8 8" fill="none" stroke="#fff" stroke-width="3.4" stroke-linecap="round" stroke-linejoin="round"/></svg>
      <h1 class="app-bar__title">Coupons App</h1>
      <svg class="app-bar__settings" width="40" height="40" viewBox="0 0 40 40"><circle cx="20" cy="20" r="17.5" fill="none" stroke="#fff" stroke-width="3"/><circle cx="20" cy="20" r="9" fill="none" stroke="#fff" stroke-width="5" stroke-dasharray="3.4 2.2"/><circle cx="20" cy="20" r="6.5" fill="#fff"/><circle cx="20" cy="20" r="3" fill="var(--brand-green)"/></svg>
    </header>
    <p class="session-note">Logged in as Sample Name</p>
    <div class="session-rule"></div>
    <h2 class="page-title">Business Search</h2>
    <div class="search-field">
      <span class="search-field__text">Tap here to edit text &nbsp;. . .</span>
      <svg class="search-field__icon" width="26" height="24" viewBox="0 0 26 24"><circle cx="10" cy="10" r="7" fill="none" stroke="var(--icon-faint)" stroke-width="3"/><path d="M15 15l8 7" stroke="var(--icon-faint)" stroke-width="4" stroke-linecap="round"/></svg>
    </div>
    <p class="hint">You can search businesses by name etc and some sample text comes here . . .</p>
    <div class="empty-row">
      <div class="empty-row__mark"></div>
      <p class="empty-row__title">No Results</p>
      <p class="empty-row__note">Check spellings and some more text</p>
    </div>
  </section>

  <!-- Screen: results -->
  <section class="screen screen--results">
    <header class="app-bar">
      <svg class="app-bar__back" width="40" height="40" viewBox="0 0 40 40"><circle cx="20" cy="20" r="17.5" fill="none" stroke="#fff" stroke-width="3"/><path d="M11 20h18M18 12l-8 8 8 8" fill="none" stroke="#fff" stroke-width="3.4" stroke-linecap="round" stroke-linejoin="round"/></svg>
      <h1 class="app-bar__title">Coupons App</h1>
      <svg class="app-bar__settings" width="40" height="40" viewBox="0 0 40 40"><circle cx="20" cy="20" r="17.5" fill="none" stroke="#fff" stroke-width="3"/><circle cx="20" cy="20" r="9" fill="none" stroke="#fff" stroke-width="5" stroke-dasharray="3.4 2.2"/><circle cx="20" cy="20" r="6.5" fill="#fff"/><circle cx="20" cy="20" r="3" fill="var(--brand-green)"/></svg>
    </header>
    <p class="session-note">Logged in as Sample Name</p>
    <div class="session-rule"></div>
    <h2 class="page-title">Business Search</h2>
    <div class="search-field">
      <span class="search-field__text">Random Business</span>
      <svg class="search-field__icon" width="26" height="24" viewBox="0 0 26 24"><circle cx="10" cy="10" r="7" fill="none" stroke="var(--icon-faint)" stroke-width="3"/><path d="M15 15l8 7" stroke="var(--icon-faint)" stroke-width="4" stroke-linecap="round"/></svg>
    </div>
    <div class="results-summary">
      <p class="results-summary__count">05 Search Results . . .</p>
      <p class="results-summary__tip">Slide the results for more options</p>
    </div>
    <ul class="result-list">
      <li class="result"><div class="result__logo logo-blue"></div><p class="result__name">Business one</p><p class="result__meta">Lorem ipsum dolor sit amet</p></li>
      <li class="result"><div class="result__logo logo-violet"></div><p class="result__name">Sample Name</p><p class="result__meta">Lorem Ipsum dolor , sit, amet</p></li>
      <li class="result"><div class="result__logo logo-grey"></div><p class="result__name">Lorem ipsum</p><p class="result__meta">Sample text placed here</p></li>
      <li class="result"><div class="result__logo logo-peach"></div><p class="result__name">Other name</p><p class="result__meta">sample , text , placed, here</p></li>
    </ul>
    <div class="show-all">
      <svg width="24" height="16" viewBox="0 0 24 16"><path d="M1 2l11 5 11-5v5l-11 5-11-5z" fill="#c4c4c4"/><path d="M1 8l11 5 11-5v3l-11 5-11-5z" fill="#c4c4c4"/></svg>
      <span>Show all results</span>
    </div>
  </section>

  <!-- Screen: swiped result -->
  <section class="screen screen--swiped">
    <header class="app-bar">
      <svg class="app-bar__back" width="40" height="40" viewBox="0 0 40 40"><circle cx="20" cy="20" r="17.5" fill="none" stroke="#fff" stroke-width="3"/><path d="M11 20h18M18 12l-8 8 8 8" fill="none" stroke="#fff" stroke-width="3.4" stroke-linecap="round" stroke-linejoin="round"/></svg>
      <h1 class="app-bar__title">Coupons App</h1>
      <svg class="app-bar__settings" width="40" height="40" viewBox="0 0 40 40"><circle cx="20" cy="20" r="17.5" fill="none" stroke="#fff" stroke-width="3"/><circle cx="20" cy="20" r="9" fill="none" stroke="#fff" stroke-width="5" stroke-dasharray="3.4 2.2"/><circle cx="20" cy="20" r="6.5" fill="#fff"/><circle cx="20" cy="20" r="3" fill="var(--brand-green)"/></svg>
    </header>
    <p class="session-note">Logged in as Sample Name</p>
    <div class="session-rule"></div>
    <h2 class="page-title">Business Search</h2>
    <div class="search-field">
      <span class="search-field__text">Random Business</span>
      <svg class="search-field__icon" width="26" height="24" viewBox="0 0 26 24"><circle cx="10" cy="10" r="7" fill="none" stroke="var(--icon-faint)" stroke-width="3"/><path d="M15 15l8 7" stroke="var(--icon-faint)" stroke-width="4" stroke-linecap="round"/></svg>
    </div>
    <div class="results-summary">
      <p class="results-summary__count">05 Search Results . . .</p>
      <p class="results-summary__tip">Slide the results for more options</p>
    </div>
    <ul class="result-list">
      <li class="result result--swiped">
        <div class="result__actions">
          <span class="action-button action-button--edit"><svg width="22" height="26" viewBox="0 0 22 26"><path d="M14 2l6 5-11 13-6 2 1-6z" fill="var(--icon-faint)"/><path d="M2 24h18" stroke="var(--icon-faint)" stroke-width="2"/></svg></span>
          <span class="action-button action-button--delete"><svg width="22" height="28" viewBox="0 0 22 28"><rect x="7" y="1" width="8" height="3" fill="var(--icon-faint)"/><rect x="1" y="4" width="20" height="3" fill="var(--icon-faint)"/><rect x="3" y="8" width="16" height="19" fill="none" stroke="var(--icon-faint)" stroke-width="2"/><path d="M7 11v13M11 11v13M15 11v13" stroke="var(--icon-faint)" stroke-width="2"/></svg></span>
        </div>
        <div class="result__logo logo-blue"></div><p class="result__name">Business one</p><p class="result__meta">Lorem ipsum dolor sit amet</p>
      </li>
      <li class="result"><div class="result__logo logo-violet"></div><p class="result__name">Sample Name</p><p class="result__meta">Lorem Ipsum dolor , sit, amet</p></li>
      <li class="result"><div class="result__logo logo-grey"></div><p class="result__name">Lorem ipsum</p><p class="result__meta">Sample text placed here</p></li>
      <li class="result"><div class="result__logo logo-peach"></div><p class="result__name">Other name</p><p class="result__meta">sample , text , placed, here</p></li>
    </ul>
    <div class="show-all">
      <svg width="24" height="16" viewBox="0 0 24 16"><path d="M1 2l11 5 11-5v5l-11 5-11-5z" fill="#c4c4c4"/><path d="M1 8l11 5 11-5v3l-11 5-11-5z" fill="#c4c4c4"/></svg>
      <span>Show all results</span>
    </div>
  </section>

</main>
</body>
</html>
```